Business Card for TLK Field Services

Would like a large logo on one side. On the other side, logo on one side and company phone number, address, and email on the other side. I don't have a logo so please create one for us.
Updates
I don't have a logo, so please create one for us.
Target Market(s)
Land Surveying
Industry/Entity Type
Surveyor
Contact Information for Business Card
Would like a large logo on one side. On the other side, logo on one side and company phone number, address, and email on the other side
Requirements
Nice to have
- would like the initials to be incorporated with the logo

```html
<!DOCTYPE html>
<html lang="en">
<head>
<meta charset="UTF-8">
<title>TLK Field Services – Business Card</title>
<link href="https://fonts.googleapis.com/css2?family=Questrial&display=swap" rel="stylesheet">
<style>
  :root {
    --bg: #3a3633;
    --card-white: #f2f2f2;
    --card-black: #1c1c1c;
    --swoosh-dark: #2a2a2a;
    --swoosh-mid: #555555;
    --swoosh-light: #8a8a8a;
    --ink: #2b2b2b;
    --logo-light: #d9d9d9;
  }
  * { margin: 0; padding: 0; box-sizing: border-box; }
  html, body { width: 1200px; height: 727px; overflow: hidden; }
  body {
    background: var(--bg);
    font-family: "Questrial", sans-serif;
    position: relative;
  }
  .card {
    position: absolute;
    top: 210px;
    width: 520px;
    height: 300px;
    border-radius: 6px;
    overflow: hidden;
  }
  .card-front { left: 50px; background: var(--card-white); }
  .card-back { left: 630px; background: var(--card-black); }

  .front-swoosh { position: absolute; inset: 0; width: 100%; height: 100%; }

  .front-logo {
    position: absolute;
    left: 32px;
    top: 30px;
    font-size: 24px;
    color: var(--ink);
    letter-spacing: 0.5px;
  }
  .holder { position: absolute; left: 32px; top: 112px; color: var(--ink); }
  .holder-name { font-size: 22px; }
  .holder-title { font-size: 13px; margin-top: 2px; }

  .contact-list { list-style: none; position: absolute; left: 32px; top: 178px; color: var(--ink); font-size: 14px; }
  .contact-list li { display: flex; align-items: center; gap: 10px; height: 24px; }
  .contact-list svg { width: 14px; height: 14px; fill: var(--ink); }

  .back-logo {
    position: absolute;
    inset: 0;
    display: flex;
    align-items: center;
    justify-content: center;
    font-size: 40px;
    color: var(--logo-light);
    letter-spacing: 1px;
  }
</style>
</head>
<body>
  <section class="card card-front">
    <svg class="front-swoosh" viewBox="0 0 520 300" preserveAspectRatio="none" aria-hidden="true">
      <path d="M300 0 L520 0 L520 300 L430 300 C470 210 430 80 300 0 Z" fill="var(--swoosh-light)"/>
      <path d="M340 0 L520 0 L520 300 L450 300 C490 200 450 70 340 0 Z" fill="var(--swoosh-mid)"/>
      <path d="M380 0 L520 0 L520 300 L470 300 C500 190 470 150 430 150 C470 120 450 60 380 0 Z" fill="var(--swoosh-dark)"/>
    </svg>
    <div class="front-logo">TLK Field Services</div>
    <div class="holder">
      <div class="holder-name">Your Name</div>
      <div class="holder-title">Job title</div>
    </div>
    <ul class="contact-list">
      <li>
        <svg viewBox="0 0 16 16"><path d="M2 6 C2 3 14 3 14 6 L14 8 L11 8 L11 6.5 L5 6.5 L5 8 L2 8 Z M4 9 L12 9 L13 14 L3 14 Z"/></svg>
        000 000 0000
      </li>
      <li>
        <svg viewBox="0 0 16 16"><path d="M1 3 L15 3 L15 13 L1 13 Z M2 4 L8 9 L14 4 Z" fill-rule="evenodd"/></svg>
        youremail@tlkfield.com
      </li>
      <li>
        <svg viewBox="0 0 16 16"><circle cx="8" cy="8" r="6.5" fill="none" stroke="var(--ink)" stroke-width="1.3"/><path d="M1.5 8 H14.5 M8 1.5 C4.5 5 4.5 11 8 14.5 M8 1.5 C11.5 5 11.5 11 8 14.5" fill="none" stroke="var(--ink)" stroke-width="1.1"/></svg>
        tlkfieldservices.com
      </li>
    </ul>
  </section>

  <section class="card card-back">
    <div class="back-logo">TLK Field Services</div>
  </section>
</body>
</html>
```